Prestige Car Bodyshop Business Card

We are a car bodyshop based in the UK. Our customer base is mainly prestige high-value vehicles. I am looking for a classy and stylish business card design for my staff to give out to customers, with their direct email and phone number, as well as our main email and phone number with address details

I am also looking to have a general business card design with just our main company address and contact details, but also have a space to add a manufacturer approval logo (i.e Velmora, Orek, Tovalo etc... logo) in the corner somewhere.

I do not particularly want any outlines or pictures of cars on the card, I would just like a quality high-end look.

Please feel free to get in touch if you have any questions or queries?

Many Thanks

Malcolm

Target Market(s)

Prestige vehicle owners

Industry/Entity Type

Automotive

Contact Information for Business Card

I am looking for a classy and stylish business card design for my staff to give out to customers, with their direct email and phone number, as well as our main email and phone number with address details

Font styles to use
Sans Serif

Colors

Designer to choose colors to be used in the design.

Requirements
Nice to have
• I do not particularly want any outlines or pictures of cars on the card, I would just like a quality high-end look.

```html
<!DOCTYPE html>
<html lang="en">
<head>
<meta charset="utf-8">
<title>RK Ashby Accident Repair Centre – Business Card</title>
<link rel="stylesheet" href="https://fonts.googleapis.com/css2?family=Questrial&display=swap">
<style>
  :root {
    --page-bg: #ebebeb;
    --card-white: #ffffff;
    --brand-navy: #2a2344;
    --ink-light: #ffffff;
    --ink-soft: #cfcadf;
    --maker-grey: #6a6385;
  }
  * { margin: 0; padding: 0; box-sizing: border-box; }
  html, body { width: 1200px; height: 1000px; overflow: hidden; }
  body {
    background: var(--page-bg);
    font-family: "Questrial", sans-serif;
    position: relative;
  }
  .card {
    position: absolute;
    left: 272px;
    width: 665px;
    height: 379px;
  }
  .card-front { top: 56px; background: var(--card-white); }
  .card-back { top: 519px; background: var(--brand-navy); color: var(--ink-light); }

  .brand-mark {
    position: absolute;
    left: 392px;
    top: 33px;
    width: 88px;
    height: 88px;
    border-radius: 50%;
    background: var(--brand-navy);
  }
  .brand-name {
    position: absolute;
    left: 490px;
    top: 30px;
    font-size: 28px;
    letter-spacing: 0.5px;
    color: var(--brand-navy);
  }
  .brand-rule {
    position: absolute;
    left: 490px;
    top: 68px;
    width: 158px;
    height: 1.5px;
    background: var(--brand-navy);
  }
  .brand-tagline {
    position: absolute;
    left: 490px;
    top: 75px;
    font-size: 11px;
    letter-spacing: 0.9px;
    color: var(--brand-navy);
    white-space: nowrap;
  }

  .contact-block {
    position: absolute;
    left: 227px;
    top: 128px;
    padding-left: 11px;
    border-left: 1.5px solid var(--ink-light);
    font-style: normal;
  }
  .address {
    font-size: 21px;
    line-height: 26px;
    letter-spacing: 1px;
    word-spacing: 4px;
    white-space: nowrap;
  }
  .contact-lines {
    margin-top: 8px;
    font-size: 14px;
    line-height: 20px;
    letter-spacing: 0.8px;
    color: var(--ink-soft);
    white-space: nowrap;
  }

  .approved-makers {
    position: absolute;
    left: 0;
    right: 0;
    top: 322px;
    display: flex;
    justify-content: space-around;
    list-style: none;
    padding: 0 6px;
  }
  .approved-makers li {
    font-size: 14px;
    letter-spacing: 1.5px;
    text-transform: uppercase;
    color: var(--maker-grey);
  }
</style>
</head>
<body>
  <section class="card card-front" aria-label="Business card front">
    <div class="brand-mark"></div>
    <div class="brand-name">RK ASHBY</div>
    <div class="brand-rule"></div>
    <div class="brand-tagline">ACCIDENT REPAIR CENTRE</div>
  </section>

  <section class="card card-back" aria-label="Business card back">
    <address class="contact-block">
      <div class="address">
        48 Fenmore Road<br>
        Alder Vale Lane<br>
        London SE9 4QT
      </div>
      <div class="contact-lines">
        T 020 7946 0318<br>
        E info@rkashbyrepairs.co.uk
      </div>
    </address>
    <ul class="approved-makers">
      <li>Castellan</li>
      <li>Orek</li>
      <li>Velmora</li>
      <li>Halden</li>
      <li>Tovalo</li>
      <li>Sorai</li>
    </ul>
  </section>
</body>
</html>
```